Munchcart

App Design for a an application on which you can order take aways from restaurants close to you.
(similar app : https://appvault.example/lu/app/grubniq-pizza-burger-sushi/id583017264?l=en&mt=8 )

Logo is a taxi (psd of taxi an font attached)

Attached a draft mockup showing the screens needed.

Screens needed :

1. Splash Screen
2. Select you restaurant screen
3. Select your dish (meat, pizza, pasta....)
4. Select your extras (exta cheese, garlik etc...)
5. Exit screen with total amount and confirmation
6. Subscribe Screen where people have to register the first time.

Target Market(s)

age 14-54

Industry/Entity Type

Restaurant

Requirements
Must have
• Wood elements

```html
<!DOCTYPE html>
<html lang="en">
<head>
<meta charset="utf-8">
<title>Munchcart – Register</title>
<link rel="stylesheet" href="https://fonts.googleapis.com/css2?family=Questrial&display=swap">
<style>
  :root {
    --screen-black: #0b0a0c;
    --night-navy: #1d2634;
    --dusk-blue: #5f7f9c;
    --amber: #c9762f;
    --ember: #8a3f1c;
    --wet-asphalt: #3a2a24;
    --text-white: #ffffff;
    --field-fill: rgba(255, 255, 255, 0.28);
    --placeholder: rgba(255, 255, 255, 0.72);
    --statusbar: rgba(0, 0, 0, 0.72);
  }
  * { box-sizing: border-box; margin: 0; padding: 0; }
  html, body {
    width: 685px;
    height: 1200px;
    overflow: hidden;
    background: var(--screen-black);
    font-family: "Questrial", "Century Gothic", sans-serif;
    color: var(--text-white);
  }
  .register-screen {
    position: relative;
    width: 685px;
    height: 1200px;
    overflow: hidden;
  }
  .backdrop {
    position: absolute;
    inset: 0;
    background:
      radial-gradient(ellipse 55% 30% at 88% 8%, rgba(95, 127, 156, 0.85), transparent 70%),
      radial-gradient(ellipse 70% 30% at 55% 78%, rgba(201, 118, 47, 0.7), transparent 75%),
      linear-gradient(180deg, var(--night-navy) 0%, #241c1c 30%, var(--ember) 52%, var(--amber) 66%, var(--wet-asphalt) 100%);
  }
  .status-bar {
    position: absolute;
    top: 0; left: 0; right: 0;
    height: 37px;
    background: var(--statusbar);
    display: flex;
    align-items: center;
    justify-content: space-between;
    padding: 0 14px;
    font-size: 17px;
    letter-spacing: 0.5px;
  }
  .status-left { display: flex; align-items: center; gap: 8px; }
  .status-time { position: absolute; left: 50%; transform: translateX(-50%); }
  .brand {
    position: absolute;
    top: 360px;
    left: 0; right: 0;
    text-align: center;
    font-size: 58px;
    letter-spacing: 1px;
  }
  .headline {
    position: absolute;
    top: 528px;
    left: 0; right: 0;
    text-align: center;
    font-size: 62px;
    font-weight: 400;
  }
  .register-form {
    position: absolute;
    top: 632px;
    left: 70px;
    width: 525px;
    display: flex;
    flex-direction: column;
    gap: 43px;
  }
  .text-field {
    height: 70px;
    background: var(--field-fill);
    display: flex;
    align-items: center;
    padding-left: 22px;
    font-size: 30px;
    color: var(--placeholder);
  }
</style>
</head>
<body>
  <main class="register-screen">
    <div class="backdrop" role="img" aria-label="Blurred night street photo with glowing orange city lights reflected on wet pavement"></div>

    <header class="status-bar">
      <div class="status-left">
        <svg width="24" height="14" viewBox="0 0 24 14" aria-hidden="true">
          <rect x="0" y="10" width="3" height="4" fill="#fff"/>
          <rect x="5" y="7" width="3" height="7" fill="#fff"/>
          <rect x="10" y="5" width="3" height="9" fill="#fff"/>
          <rect x="15" y="2" width="3" height="12" fill="#fff"/>
          <rect x="20" y="0" width="3" height="14" fill="#fff"/>
        </svg>
        <span>NORTHCELL</span>
        <span>3G</span>
      </div>
      <span class="status-time">4:20 AM</span>
      <svg width="52" height="18" viewBox="0 0 52 18" aria-hidden="true">
        <circle cx="8" cy="9" r="7" fill="#fff"/>
        <rect x="18" y="3" width="28" height="12" rx="2" fill="none" stroke="#fff" stroke-width="1.5"/>
        <rect x="20" y="5" width="24" height="8" fill="#fff"/>
        <rect x="47" y="6.5" width="2.5" height="5" fill="#fff"/>
      </svg>
    </header>

    <div class="brand">Munchcart</div>

    <h1 class="headline">Register now!</h1>

    <form class="register-form">
      <div class="text-field">username</div>
      <div class="text-field">password</div>
    </form>
  </main>
</body>
</html>
```